RW Skyline Imaging Web Site design

I am looking for a responsive single page website deign for rwskylineimages.example. This is a drone based aerial photography and cinematography business. It should have an about us section, a services section that contains photograph service, Video footage, and Aerial mapping all under the services section, a pricing section, and then a contact page for customers to contact us.

Coding

Coded - Design and coding required

Number of Pages Required

1 page

Font styles to use
Sans Serif

Colors

Designer to choose colors to be used in the design.

Requirements
Must have
• Responsive design. About us section, services section, pricing section under the services links, and contact us section, that links to a submission page where they can send Name, address, email, and comments on what they are interested in.
• See flyquad7x.example - looking for similar design.
Should not have
• clutter, or too busy design

```html
<!DOCTYPE html>
<html lang="en">
<head>
<meta charset="utf-8">
<title>RW Skyline Imaging</title>
<link href="https://fonts.googleapis.com/css2?family=Raleway:wght@400;500;600;700&family=Lato:wght@400;700&display=swap" rel="stylesheet">
<style>
:root{
  --orange:#f7941d;
  --orange-dark:#e07f0c;
  --ink:#222;
  --text:#555;
  --white:#fff;
  --footer:#333333;
  --footer-panel:#262626;
  --player:#1b1b1b;
}
*{box-sizing:border-box;margin:0;padding:0}
html,body{width:1200px;height:4147px;overflow:hidden}
body{font-family:'Lato',sans-serif;color:var(--text);background:var(--white);position:relative}
h1,h2,h3,h4{font-family:'Raleway',sans-serif;font-weight:500}
.section-title{text-align:center;font-size:36px;color:var(--ink)}
.section-title span{color:var(--orange)}
.title-mark{display:block;margin:10px auto 0;width:120px;height:14px}

/* header */
.site-header{position:absolute;top:0;left:0;width:1200px;height:83px;display:flex;align-items:center;justify-content:space-between;padding:0 50px 0 160px}
.brand{display:flex;align-items:center;gap:12px;font-family:'Raleway',sans-serif;font-size:20px;letter-spacing:3px;color:var(--ink)}
.brand-dot{width:14px;height:14px;border-radius:50%;background:var(--orange)}
.main-nav{display:flex;gap:0}
.main-nav a{display:block;padding:0 22px;font-family:'Raleway',sans-serif;font-size:14px;color:var(--ink);text-decoration:none;border-left:1px solid #ddd;line-height:20px}
.main-nav a:first-child{border-left:none}
.main-nav a.active{color:var(--orange);border-bottom:2px solid var(--orange)}

/* hero */
.hero{position:absolute;top:83px;left:0;width:1200px;height:506px;background:linear-gradient(180deg,#3e4a3a 0%,#2d3a2e 45%,#48503f 100%);text-align:center;color:var(--white)}
.hero h1{padding-top:178px;font-size:36px;line-height:46px;font-weight:600;text-shadow:0 2px 6px rgba(0,0,0,.5)}
.btn{display:inline-block;background:var(--orange);color:var(--white);font-family:'Raleway',sans-serif;font-weight:600;text-decoration:none}
.hero .btn{margin-top:18px;font-size:22px;padding:10px 22px;border-radius:3px}

/* about */
.about{position:absolute;top:620px;left:0;width:1200px}
.about p{width:860px;margin:18px auto 0;text-align:center;font-size:12.5px;line-height:20px}
.about .lead{margin-top:30px}

.player{position:absolute;left:174px;width:852px;height:575px;background:var(--player);border-radius:8px;overflow:hidden;box-shadow:0 4px 12px rgba(0,0,0,.35)}
.player .frame{position:absolute;inset:0 0 68px 0}
.play-big{position:absolute;left:50%;top:50%;width:110px;height:74px;margin:-64px 0 0 -55px;background:rgba(20,20,20,.85);border-radius:14px}
.play-big::after{content:"";position:absolute;left:44px;top:20px;border-left:30px solid #fff;border-top:17px solid transparent;border-bottom:17px solid transparent}
.controls{position:absolute;left:0;right:0;bottom:0;height:68px;background:linear-gradient(#2a2a2a,#111);display:flex;align-items:center;padding:0 24px;gap:22px}
.controls .bar{flex:1;height:12px;background:#444;border-radius:6px;position:relative;margin-right:40px}
.controls .bar i{position:absolute;left:0;top:0;bottom:0;width:42%;background:#c8201c;border-radius:6px}

/* services */
.services{position:absolute;top:1535px;left:0;width:1200px;height:572px;background:linear-gradient(180deg,#25313c 0%,#3b4856 60%,#2a323b 100%);color:var(--white)}
.services .section-title{color:var(--white);padding-top:68px;font-size:34px}
.services .section-title span{color:var(--orange)}
.service-row{position:absolute;top:185px;left:174px;width:852px;display:flex;justify-content:space-between}
.service-card{width:270px;height:285px;text-align:center;padding-top:25px}
.service-card.featured{background:rgba(200,200,200,.55)}
.icon-ring{width:100px;height:100px;margin:0 auto;border-radius:50%;background:var(--white);border:6px solid var(--orange);display:flex;align-items:center;justify-content:center}
.service-card h3{font-size:19px;margin-top:20px;color:var(--white)}
.service-card .price{font-family:'Raleway',sans-serif;font-size:30px;margin-top:8px}
.service-card .price sup,.service-card .price small{font-size:13px}
.service-card p{font-size:12.5px;line-height:17px;margin:12px 22px 0}
.service-card.featured p{color:#444}
.service-card.featured h3{color:#222;margin-top:6px}
.service-card.featured .price{color:#222}

/* recent work */
.work{position:absolute;top:2130px;left:0;width:1200px}
.work .caption{position:absolute;top:710px;left:174px;width:852px;text-align:center;font-size:12.5px;line-height:19px;color:#333}
.thumbs{position:absolute;top:773px;left:163px;width:874px;display:flex;justify-content:space-between}
.thumb{width:283px}
.thumb .mini{position:relative;height:194px;background:#1b1b1b;border:1px solid #ccc;overflow:hidden}
.thumb .mini .frame{position:absolute;inset:0 0 22px 0}
.thumb .mini .mbar{position:absolute;left:0;right:0;bottom:0;height:22px;background:#111;display:flex;align-items:center;gap:6px;padding:0 8px}
.mbar b{display:block;width:0;height:0;border-left:8px solid #fff;border-top:5px solid transparent;border-bottom:5px solid transparent}
.mbar span{flex:1;height:5px;background:#444;position:relative}
.mbar span i{position:absolute;left:0;top:0;bottom:0;width:45%;background:#c8201c}
.mini .mplay{position:absolute;left:50%;top:45%;width:44px;height:30px;margin:-15px 0 0 -22px;background:rgba(20,20,20,.85);border-radius:6px}
.mini .mplay::after{content:"";position:absolute;left:17px;top:8px;border-left:13px solid #fff;border-top:7px solid transparent;border-bottom:7px solid transparent}
.thumb p{font-size:12.5px;line-height:17px;color:#333;margin-top:10px}

/* pilots */
.pilots{position:absolute;top:3225px;left:0;width:1200px}
.lead-pilot{position:absolute;top:93px;left:171px;width:222px;height:222px;border-radius:50%;border:8px solid var(--orange);background:radial-gradient(circle at 50% 40%,#d9dde2,#8a97a6)}
.pilot-bio{position:absolute;top:128px;left:430px;width:600px}
.pilot-bio h4{font-size:16px;color:#222}
.pilot-bio h4 small{font-size:13px;color:#666;font-weight:400}
.pilot-bio p{font-size:12.5px;line-height:18px;margin-top:8px;color:#444}
.crew{position:absolute;top:285px;left:330px;display:flex;gap:18px}
.crew-member{width:100px;text-align:center;font-size:11px;line-height:13px;color:#444}
.avatar{width:74px;height:74px;margin:0 auto 6px;border-radius:50%;border:3px solid #fff;box-shadow:0 0 0 2px #ccc;background:radial-gradient(circle at 50% 40%,#c9ced5,#56606c)}
.crew-member:first-child .avatar{background:radial-gradient(circle at 50% 40%,#e4e6ea,#a8b0ba)}

/* cta */
.cta{position:absolute;top:3658px;left:0;width:1200px;height:149px;background:var(--orange);display:flex;align-items:center;justify-content:space-between;padding:0 200px 0 185px}
.cta h2{color:var(--white);font-size:28px;font-weight:500}
.cta .btn{background:#1f1f1f;font-family:'Lato',sans-serif;font-weight:400;font-size:18px;padding:8px 12px}

/* footer */
.site-footer{position:absolute;top:3807px;left:0;width:1200px;height:340px;background:var(--footer);color:#ddd}
.contact-panel{position:absolute;left:166px;top:0;width:276px;height:340px;background:var(--footer-panel);padding:30px 22px}
.contact-panel h3{font-size:24px;color:var(--white);margin-bottom:14px}
.field{height:28px;background:#555;margin-bottom:9px;font-size:11px;color:#eee;padding:6px 8px}
.field.area{height:70px}
.submit{margin-top:14px;width:90px;height:26px;background:#fff;color:#222;font-size:13px;text-align:center;line-height:26px}
.foot-col{position:absolute;top:38px}
.foot-col h4{font-size:16px;color:#fff;font-weight:500}
.quick{left:476px;width:125px;text-align:center}
.quick h4::after{content:"";display:block;width:90px;height:1px;background:#888;margin:10px auto 8px}
.quick a{display:block;color:#ddd;text-decoration:none;font-size:12px;line-height:23px}
.details{left:640px;width:200px}
.details ul{list-style:none;margin-top:22px;font-size:11.5px;line-height:15px}
.details li{display:flex;gap:10px;margin-bottom:16px}
.details li strong{color:#fff}
.follow{left:880px;width:200px;text-align:center}
.socials{display:flex;justify-content:center;gap:8px;margin-top:18px}
.socials i{display:block;width:30px;height:30px;border:2px solid #ddd;border-radius:50%}
.foot-brand{margin-top:38px;font-family:'Raleway',sans-serif;font-size:14px;letter-spacing:3px;color:#ddd}
.copyright{position:absolute;left:482px;top:297px;font-size:11.5px;color:#ddd}
</style>
</head>
<body>

<header class="site-header">
  <div class="brand"><span class="brand-dot"></span>RW Skyline Imaging</div>
  <nav class="main-nav">
    <a href="#" class="active">Home</a><a href="#">About Us</a><a href="#">Services</a><a href="#">Pricing</a><a href="#">Pilots</a><a href="#">Contact Us</a>
  </nav>
</header>

<section class="hero" role="img" aria-label="Aerial photo of a campus and green hillside seen from a drone">
  <h1>We Are In A Drone Based<br>Aerial Photography And Cinematography Business</h1>
  <a class="btn" href="#">Learn More</a>
</section>

<section class="about">
  <h2 class="section-title"><span>About RW</span> Skyline Imaging</h2>
  <svg class="title-mark" viewBox="0 0 120 14"><path d="M0 4h48l12 8 12-8h48" fill="none" stroke="#f7941d" stroke-width="2"/></svg>
  <p class="lead">We capture homes, events, farms and building sites from the air with licensed pilots and stable camera drones. Every flight is planned around light, weather and local rules so each frame is sharp and safe. Our team edits stills and footage in house and delivers files ready for listings, brochures, social posts and presentations within a few working days.</p>
  <p>From a single listing shoot to a full season of site progress reports, we tailor each package to what you need to show. Tell us the location, the story and the deadline, and we will suggest flight times, angles and formats. Clear pricing, friendly support and quick turnaround are part of every booking we take on.</p>
  <div class="player" style="top:276px">
    <div class="frame" role="img" aria-label="Video still of a couple in a park with a drone on the grass" style="background:linear-gradient(180deg,#3d5a34 0%,#6f8f4a 55%,#4e7a32 100%)"></div>
    <div class="play-big"></div>
    <div class="controls">
      <svg width="26" height="28" viewBox="0 0 26 28"><path d="M2 2l22 12L2 26z" fill="#fff"/></svg>
      <svg width="28" height="24" viewBox="0 0 28 24"><path d="M2 8h6l8-6v20l-8-6H2z" fill="#fff"/><path d="M20 7q4 5 0 10" stroke="#fff" stroke-width="2" fill="none"/></svg>
      <div class="bar"><i></i></div>
      <svg width="26" height="26" viewBox="0 0 26 26"><path d="M15 2h9v9M24 2l-9 9M11 24H2v-9M2 24l9-9" stroke="#fff" stroke-width="2.5" fill="none"/></svg>
    </div>
  </div>
</section>

<section class="services" role="region" aria-label="Services over a city skyline seen from above">
  <h2 class="section-title"><span>Photography, Video Footage,</span> and Aerial 3D Mapping</h2>
  <svg class="title-mark" viewBox="0 0 120 14"><path d="M0 4h48l12 8 12-8h48" fill="none" stroke="#f7941d" stroke-width="2"/></svg>
  <div class="service-row">
    <article class="service-card featured">
      <div class="icon-ring"><svg width="40" height="34" viewBox="0 0 40 34"><rect x="2" y="8" width="36" height="24" rx="4" fill="none" stroke="#222" stroke-width="3"/><path d="M13 8l3-6h8l3 6" fill="none" stroke="#222" stroke-width="3"/><circle cx="20" cy="20" r="7" fill="none" stroke="#222" stroke-width="3"/></svg></div>
      <div class="price"><sup>$</sup>200<small>.00</small></div>
      <h3>Photograph Service</h3>
      <p>High resolution aerial stills of homes, land and events, edited and delivered.</p>
    </article>
    <article class="service-card">
      <div class="icon-ring"><svg width="40" height="34" viewBox="0 0 40 34"><rect x="2" y="2" width="36" height="30" fill="none" stroke="#222" stroke-width="3"/><path d="M8 2v30M32 2v30" stroke="#222" stroke-width="2"/><path d="M16 11l9 6-9 6z" fill="#222"/></svg></div>
      <h3>Video Footage</h3>
      <p>Smooth cinematic flyovers and reveals, shot in 4K and cut to music for your project or listing page.</p>
    </article>
    <article class="service-card">
      <div class="icon-ring"><svg width="44" height="36" viewBox="0 0 44 36"><path d="M2 10l12-5 16 5 12-5v22l-12 5-16-5-12 5z" fill="none" stroke="#222" stroke-width="3"/><circle cx="22" cy="14" r="5" fill="none" stroke="#222" stroke-width="3"/></svg></div>
      <h3>Aerial 3D Mapping</h3>
      <p>Accurate maps and 3D models of sites, roofs and fields for planning, survey and progress reports.</p>
    </article>
  </div>
</section>

<section class="work">
  <h2 class="section-title"><span>Recent</span> Work</h2>
  <svg class="title-mark" viewBox="0 0 120 14"><path d="M0 4h48l12 8 12-8h48" fill="none" stroke="#f7941d" stroke-width="2"/></svg>
  <div class="player" style="top:110px">
    <div class="frame" role="img" aria-label="Video still of a large house and garden with a drone in the sky" style="background:linear-gradient(180deg,#8fb5d8 0%,#a9c2d6 35%,#7d8a72 60%,#4f7a3a 100%)"></div>
    <div class="play-big"></div>
    <div class="controls">
      <svg width="26" height="28" viewBox="0 0 26 28"><path d="M2 2l22 12L2 26z" fill="#fff"/></svg>
      <svg width="28" height="24" viewBox="0 0 28 24"><path d="M2 8h6l8-6v20l-8-6H2z" fill="#fff"/><path d="M20 7q4 5 0 10" stroke="#fff" stroke-width="2" fill="none"/></svg>
      <div class="bar"><i></i></div>
      <svg width="26" height="26" viewBox="0 0 26 26"><path d="M15 2h9v9M24 2l-9 9M11 24H2v-9M2 24l9-9" stroke="#fff" stroke-width="2.5" fill="none"/></svg>
    </div>
  </div>
  <p class="caption">A recent residential shoot with sweeping orbits of the house, garden and street, filmed at golden hour for a listing video and matching still set.</p>
  <div class="thumbs">
    <div class="thumb">
      <div class="mini"><div class="frame" role="img" aria-label="Video still of a drone flying at sunset" style="background:linear-gradient(180deg,#c98b4e,#5a3a2a)"></div><div class="mplay"></div><div class="mbar"><b></b><span><i></i></span></div></div>
      <p>Sunset test flight over the coast with our new six rotor camera drone.</p>
    </div>
    <div class="thumb">
      <div class="mini"><div class="frame" role="img" aria-label="Video still of a fixed wing mapping drone" style="background:linear-gradient(180deg,#f2f2f2,#9aa38c)"></div><div class="mplay"></div><div class="mbar"><b></b><span><i></i></span></div></div>
      <p>Mapping run across a farm field to build a detailed 3D surface model.</p>
    </div>
    <div class="thumb">
      <div class="mini"><div class="frame" role="img" aria-label="Video still of a crowd at an outdoor event" style="background:linear-gradient(180deg,#b8b0a4,#4c4a48)"></div><div class="mplay"></div><div class="mbar"><b></b><span><i></i></span></div></div>
      <p>Outdoor festival coverage with wide crowd shots and stage flyovers.</p>
    </div>
  </div>
</section>

<section class="pilots">
  <h2 class="section-title"><span>Our</span> Drone Pilots</h2>
  <svg class="title-mark" viewBox="0 0 120 14"><path d="M0 4h48l12 8 12-8h48" fill="none" stroke="#f7941d" stroke-width="2"/></svg>
  <div class="lead-pilot" role="img" aria-label="Portrait photo of the owner and lead pilot"></div>
  <div class="pilot-bio">
    <h4>Owen Marlow, <small>Owner / Pilot</small></h4>
    <p>Owen founded the studio after ten years in film and real estate photography. He holds a commercial drone licence, plans every flight with care and leads the editing team. He enjoys turning tricky sites into simple, striking views and works closely with each client from the first call to final delivery, making sure every shot answers the brief and arrives on time.</p>
  </div>
  <div class="crew">
    <div class="crew-member"><div class="avatar" role="img" aria-label="Portrait of Owen Marlow"></div>Owen Marlow<br>Owner / Pilot</div>
    <div class="crew-member"><div class="avatar" role="img" aria-label="Portrait of Ellis Brandt"></div>Ellis Brandt</div>
    <div class="crew-member"><div class="avatar" role="img" aria-label="Portrait of Mira Toland"></div>Mira Toland</div>
    <div class="crew-member"><div class="avatar" role="img" aria-label="Portrait of Grant Osei"></div>Grant Osei</div>
    <div class="crew-member"><div class="avatar" role="img" aria-label="Portrait of Lena Petrova"></div>Lena Petrova,<br>CPA/CA</div>
  </div>
</section>

<section class="cta">
  <h2>Have questions about drone services?</h2>
  <a class="btn" href="#">Call Us Today</a>
</section>

<footer class="site-footer">
  <div class="contact-panel">
    <h3>Contact Us</h3>
    <div class="field">Name</div>
    <div class="field">Phone</div>
    <div class="field">Email</div>
    <div class="field area">Message</div>
    <div class="submit">Submit</div>
  </div>
  <div class="foot-col quick">
    <h4>Quick links</h4>
    <a href="#">Home</a><a href="#">About Us</a><a href="#">Our Services</a><a href="#">Pricing</a><a href="#">Pilots</a><a href="#">Contact Us</a>
  </div>
  <div class="foot-col details">
    <h4>Contact Details</h4>
    <ul>
      <li><svg width="12" height="16" viewBox="0 0 12 16"><path d="M6 15S1 9 1 6a5 5 0 0 1 10 0c0 3-5 9-5 9z" fill="#ddd"/><circle cx="6" cy="6" r="2" fill="#333"/></svg><span><strong>RW Skyline Imaging</strong><br>Street Name, City Name<br>State Zipcode</span></li>
      <li><svg width="14" height="12" viewBox="0 0 14 12"><rect x="1" y="1" width="12" height="10" fill="none" stroke="#ddd" stroke-width="1.5"/><path d="M1 1l6 5 6-5" fill="none" stroke="#ddd" stroke-width="1.5"/></svg><span>hello@rwskylineimages.example</span></li>
      <li><svg width="14" height="14" viewBox="0 0 14 14"><path d="M3 1l3 3-2 2q2 3 4 4l2-2 3 3-2 2Q5 12 1 3z" fill="#ddd"/></svg><span>555-014-2290</span></li>
    </ul>
  </div>
  <div class="foot-col follow">
    <h4>Follow Us On</h4>
    <div class="socials"><i></i><i></i><i></i><i></i></div>
    <div class="foot-brand">RW Skyline Imaging</div>
  </div>
  <p class="copyright">Copyright © 2017 RW Skyline Imaging. All Rights Reserved</p>
</footer>

</body>
</html>
```